Professional banners for an eyewear company

I have 3 images which need to be made into banners. Size 990 x 370, with a 10 pixel white border at top and bottom of banner.

They all need to be adjusted to make the colours better and less bright.
All will need some writing written on them with a nice serif font.

Banner 1 text: Handcrafted luxury eyewear, with a purpose...
Banner 2 text: Half of our profits go to help malnourished children in India
Banner 3 text: 10% of your first order, use code: First Order

On our homepage these 3 banners will alternate, so they need to look good together.

Tips
Please take a look at the banners on the lumentrovic.com homepage, this is kind of how I want the text to be displayed, and they use good colours.

The backgrounds on Banners 2 & 3 can be changed.
Banner 3 background if you can change to a nice colour, as per lumentrovic.com homepage.
Updates

Hi, just a quick update, thank you for all the designs submitted so far, please keep in mind that the brand is a luxury high-end brand so designs will need to reflect this.

Industry/Entity Type

Eyewear

```html
<!DOCTYPE html>
<html lang="en">
<head>
<meta charset="utf-8">
<title>Orvelle – Handcrafted luxury eyewear</title>
<link rel="stylesheet" href="https://fonts.googleapis.com/css2?family=Roboto:wght@300;400&display=swap">
<style>
  :root {
    --page-white: #ffffff;
    --orange-deep: #d9812f;
    --orange-mid: #e48d3a;
    --amber-glow: #fbbf2e;
    --amber-soft: #f4a432;
    --rust-text: #b24d2c;
    --eyewear-white: #ffffff;
    --frame-dark: #1c120b;
    --frame-shadow: #5a3210;
  }
  * { margin: 0; padding: 0; box-sizing: border-box; }
  html, body {
    width: 1200px;
    height: 448px;
    overflow: hidden;
    background: var(--page-white);
  }
  .banner {
    position: absolute;
    top: 12px;
    left: 0;
    width: 1200px;
    height: 424px;
    overflow: hidden;
    background:
      radial-gradient(ellipse 300px 260px at 270px 170px, var(--amber-glow) 0%, var(--amber-soft) 45%, rgba(228,141,58,0) 100%),
      linear-gradient(90deg, #c8782c 0%, var(--orange-mid) 8%, var(--orange-mid) 60%, var(--orange-deep) 100%);
    font-family: "Roboto", "Helvetica Neue", Arial, sans-serif;
    font-weight: 300;
  }
  .product-photo {
    position: absolute;
    left: 80px;
    top: 120px;
    width: 410px;
    height: 215px;
    border-radius: 48% 52% 40% 44% / 50% 50% 46% 46%;
    background: radial-gradient(ellipse at 50% 45%, var(--frame-dark) 0%, rgba(28,18,11,0.85) 40%, rgba(90,50,16,0.35) 72%, rgba(90,50,16,0) 100%);
  }
  .tagline {
    position: absolute;
    line-height: 1;
    white-space: nowrap;
  }
  .tagline--lead {
    left: 527px;
    top: 140px;
    font-size: 39px;
    color: var(--rust-text);
    letter-spacing: -0.01em;
  }
  .tagline--headline {
    left: 612px;
    top: 186px;
    font-size: 70px;
    color: var(--eyewear-white);
    letter-spacing: 0.2em;
  }
  .tagline--close {
    right: 18px;
    top: 261px;
    font-size: 39px;
    color: var(--rust-text);
    letter-spacing: -0.01em;
  }
</style>
</head>
<body>
  <main class="banner">
    <div class="product-photo" role="img" aria-label="Photograph of a pair of black handcrafted Orvelle glasses floating above their reflection on a glowing amber background"></div>
    <p class="tagline tagline--lead">Handcrafted luxury</p>
    <h1 class="tagline tagline--headline" style="font-weight:300">EYEWEAR</h1>
    <p class="tagline tagline--close">with a purpose...</p>
  </main>
</body>
</html>
```